Brightwave Reach - Business Card

We need a business card for a Social Media Marketing company that specializes in online marketing for small businesses in Canada using common Social Media platforms such as Pictora, Kinloop, Blinkit & Chirpo.

I have uploaded a copy of our logo which I would like utilized in the business card. We would like the business card to be modern yet classy design.

Our website is www.brightwavereach.ca

Industry/Entity Type

Marketing

Contact Information for Business Card

Email: info@brightwavereach.ca
Website: www.brightwavereach.ca
Telephone: 604-392-5108

Colors

Designer to choose colors to be used in the design.

Requirements
Must have
• Social Media icons on reverse
• Please add some designs with color.

```html
<!DOCTYPE html>
<html lang="en">
<head>
<meta charset="utf-8">
<title>Brightwave Reach – Business Card</title>
<link href="https://fonts.googleapis.com/css2?family=Open+Sans:wght@400;600;700;800&display=swap" rel="stylesheet">
<style>
  :root {
    --page: #e4e4e2;
    --card-front: #fbfbfa;
    --card-back: #34383c;
    --ink: #1c1c1c;
    --ink-soft: #3a3a3a;
    --emboss: #0e1012;
    --bar: #2a2a2a;
  }
  * { margin: 0; padding: 0; box-sizing: border-box; }
  html, body { width: 1200px; height: 1021px; overflow: hidden; }
  body {
    background: var(--page);
    font-family: "Open Sans", Arial, sans-serif;
    color: var(--ink);
    position: relative;
  }
  .card {
    position: absolute;
    width: 540px;
    height: 310px;
    border-radius: 3px;
    box-shadow: 0 14px 30px rgba(0,0,0,0.18), 0 2px 5px rgba(0,0,0,0.12);
  }
  .card--front { left: 90px; top: 170px; background: var(--card-front); }
  .card--back { left: 570px; top: 540px; background: var(--card-back); }

  .brand {
    position: absolute;
    display: flex;
    align-items: center;
    gap: 8px;
    font-weight: 800;
    text-transform: uppercase;
    line-height: 1;
    white-space: nowrap;
  }
  .brand__mark { display: block; background: currentColor; }
  .card--front .brand { right: 30px; top: 34px; font-size: 17px; color: var(--ink); }
  .card--front .brand__mark { width: 10px; height: 10px; }

  .person {
    position: absolute;
    left: 30px;
    top: 118px;
    padding-left: 16px;
    border-left: 7px solid var(--bar);
  }
  .person__name { font-size: 19px; font-weight: 400; line-height: 1.1; }
  .person__name strong { font-weight: 700; }
  .person__title { font-size: 12px; color: var(--ink-soft); margin-top: 2px; }

  .website {
    position: absolute;
    right: 30px;
    top: 134px;
    font-size: 11px;
    color: var(--ink-soft);
  }

  .contacts {
    position: absolute;
    left: 36px;
    bottom: 40px;
    list-style: none;
    font-size: 12px;
    color: var(--ink-soft);
  }
  .contacts li { display: flex; align-items: center; gap: 12px; margin-top: 8px; }
  .contacts svg { width: 15px; height: 12px; fill: var(--ink); }

  .card--back .brand {
    left: 50%; top: 100px;
    transform: translateX(-50%);
    font-size: 32px;
    color: var(--emboss);
  }
  .card--back .brand__mark { width: 16px; height: 16px; }
  .socials {
    position: absolute;
    left: 0; right: 0; top: 180px;
    display: flex;
    justify-content: center;
    gap: 22px;
    list-style: none;
    font-size: 13px;
    font-weight: 700;
    color: var(--emboss);
  }
  .socials li { display: flex; align-items: center; gap: 6px; }
  .socials__mark { width: 12px; height: 12px; border-radius: 2px; background: currentColor; }
</style>
</head>
<body>
  <section class="card card--front" aria-label="Business card front">
    <div class="brand"><span class="brand__mark"></span>Brightwave Reach</div>
    <div class="person">
      <p class="person__name">Your <strong>Name</strong></p>
      <p class="person__title">Job Title</p>
    </div>
    <p class="website">www.brightwavereach.ca</p>
    <ul class="contacts">
      <li>
        <svg viewBox="0 0 15 12" aria-hidden="true"><path d="M0 0h15v12H0z M1.5 1.5v0.6L7.5 6.5l6-4.4v-0.6z" fill-rule="evenodd"/></svg>
        info@brightwavereach.ca
      </li>
      <li>
        <svg viewBox="0 0 15 12" aria-hidden="true"><path d="M1 3c0-2 2-3 6.5-3S14 1 14 3v1.2h-3V2.8H4v1.4H1z M3 5h9l2 7H1z"/></svg>
        604-392-5108
      </li>
    </ul>
  </section>

  <section class="card card--back" aria-label="Business card back">
    <div class="brand"><span class="brand__mark"></span>Brightwave Reach</div>
    <ul class="socials">
      <li><span class="socials__mark"></span>Kinloop</li>
      <li><span class="socials__mark"></span>Pictora</li>
      <li><span class="socials__mark"></span>Chirpo</li>
    </ul>
  </section>
</body>
</html>
```